■依頼の目的/概要
食と歯のプロがタッグを組んでチーズの虫歯予防効果(チーズは虫歯予防の最強食品だった)を一緒に学ぶ、というコンセプトで出版する電子書籍の表紙デザインをお願いします。

■本の内容
歯と食の専門家に向けてチーズの虫歯予防効果に関する情報を共有する書籍です。

■デザイン要望
1. タイトルの要素:①この書籍は誰向けか(対象)、②読むと何を得られるのか、③書いた私は誰か、これら3点が明確に伝わるよう表現ください。

2. 上の具体例は、次のようになります。
①歯と食のプロがタッグを組もう!→この本の対象は「栄養士と歯科医」
②チーズの虫歯予防効果を学ぶ本→チーズの虫歯予防効果がわかる
③歯科医師・杉浦航平*ルミナート口腔保健総合研究所→著者は歯の専門家

2. 書籍タイトルの調整:タイトルは検討中ですが、原稿の最初にあるような例を想定して書体等を含めデザインください。コンペの採択後、確定したタイトルを落とし込んで納品をお願いします。

3. 添付ファイル(書籍内容)は著者の知的財産なので守秘願います。

4. その他何かご不明な点がございましたら、お気軽にご質問下さい。

よろしくお願いいたします。
追記
1. 出版先:電子出版はVelbrixのフォリアを予定しています。
2. 調整および納品:コンペでデザインを採択後、最終的に、
①標題等テキストの確定に伴う字句の修正、および
②画像に関する調整の完了・データ引き渡し、
これらをもって納品と致します。

タイトルの視認性がフォリアショップの標準サイズで明瞭に読めるサイズである点、また、そのツカミから導入される帯部分に情報が多く、総じて「表紙」自体を読んでみたい、というモチベーションを高める工夫が秀逸でした。また、帯のキャッチについても多数ご提案を頂き、著者として大変参考となり当選とさせて頂きました。

トモリエの皆様

著者の杉浦です。

このたびは私共の電子書籍について表紙デザインのご提案を多数賜り、本当にありがとうございました。

お寄せ頂いたいずれの作品もオリジナリティに溢れ、創意工夫のご努力に対し関係者一同、深く敬意を表します。

これまで出版は内容一本で勝負してきましたが、今回の依頼を通じ「表紙は書籍の顔」というコンセプトを明確に自覚でき、著者として大変勉強になりました。あらためて皆様に厚く御礼申し上げます。

次の出版も計画中ですので、皆様には今後ともご支援のほど何卒宜しくお願い申し上げます。

```html
<!DOCTYPE html>
<html lang="ja">
<head>
<meta charset="utf-8">
<title>チーズは虫歯予防の最強食品</title>
<link href="https://fonts.googleapis.com/css2?family=M+PLUS+Rounded+1c:wght@800;900&family=Noto+Sans+JP:wght@500;700;900&display=swap" rel="stylesheet">
<style>
  :root{
    --red:#e8202a;
    --ink:#111111;
    --paper:#ffffff;
    --pink:#f08a90;
    --cheese-a:#f6b73c;
    --cheese-b:#fde9c4;
  }
  *{margin:0;padding:0;box-sizing:border-box}
  html,body{width:750px;height:1200px;overflow:hidden;background:var(--paper)}
  .cover{position:relative;width:750px;height:1200px;overflow:hidden;background:var(--paper);
    font-family:"Noto Sans JP",sans-serif;color:var(--ink)}

  .ribbon{position:absolute;left:60px;top:18px;width:636px;height:84px}
  .ribbon-text{position:absolute;left:0;top:30px;width:750px;text-align:center;
    font-weight:700;font-size:38px;letter-spacing:4px;line-height:1.2}

  .title-pill{position:absolute;left:308px;top:124px;width:188px;height:578px;border-radius:40px;background:var(--red)}

  .glyph{position:absolute;display:block;text-align:center;line-height:1;
    font-family:"M PLUS Rounded 1c",sans-serif;font-weight:900}
  .glyph.red{color:var(--red)}
  .glyph.white{color:var(--paper)}
  .glyph.black{color:var(--ink)}

  .author{position:absolute;writing-mode:vertical-rl;font-weight:700;line-height:1;white-space:nowrap}
  .author-org{left:66px;top:170px;font-size:24px;letter-spacing:5px}
  .author-role{left:36px;top:440px;font-size:26px;letter-spacing:12px}
  .author-name{position:absolute;display:block;width:48px;text-align:center;font-weight:900;font-size:44px;line-height:1}

  .band{position:absolute;left:0;top:889px;width:750px;height:311px;background:var(--red)}
  .gift{position:absolute;left:4px;top:862px;width:386px;height:58px;border:3px solid var(--ink);
    border-radius:29px;background:var(--paper);display:flex;align-items:center;padding-left:22px;
    font-weight:700;font-size:32px;line-height:1}
  .gift small{display:inline-block;font-size:17px;line-height:1;width:20px;margin-left:4px;text-align:center}
  .art{position:absolute;left:400px;top:830px;width:345px;height:160px;border-radius:30px;
    background:linear-gradient(90deg,var(--cheese-a),var(--cheese-b))}

  .lead{position:absolute;left:12px;top:962px;color:var(--paper);font-weight:700;font-size:34px;line-height:1.2}
  .catch{position:absolute;color:var(--paper);font-weight:900;font-size:80px;line-height:1;white-space:nowrap;
    -webkit-text-stroke:3px var(--ink);paint-order:stroke fill}
  .catch-1{left:6px;top:1022px}
  .catch-2{left:262px;top:1106px}
</style>
</head>
<body>
<div class="cover">
  <svg class="ribbon" viewBox="0 0 636 84" aria-hidden="true">
    <path d="M10 4 H626 L612 44 L626 80 H10 L24 44 Z" fill="none" stroke="#111" stroke-width="3" stroke-linejoin="round"/>
    <path d="M50 64 H586" stroke="#f08a90" stroke-width="6" stroke-linecap="round"/>
  </svg>
  <div class="ribbon-text">歯と食のプロ必見!</div>

  <!-- right column -->
  <span class="glyph red" style="left:505px;top:118px;width:170px;font-size:160px">チ</span>
  <span class="glyph red" style="left:505px;top:270px;width:170px;font-size:160px;writing-mode:vertical-rl">ー</span>
  <span class="glyph red" style="left:505px;top:455px;width:170px;font-size:160px">ズ</span>
  <span class="glyph red" style="left:505px;top:660px;width:170px;font-size:160px">は</span>

  <!-- centre column -->
  <div class="title-pill"></div>
  <span class="glyph white" style="left:326px;top:144px;width:150px;font-size:140px">虫</span>
  <span class="glyph white" style="left:326px;top:284px;width:150px;font-size:140px">歯</span>
  <span class="glyph white" style="left:326px;top:424px;width:150px;font-size:140px">予</span>
  <span class="glyph white" style="left:326px;top:562px;width:150px;font-size:140px">防</span>
  <span class="glyph black" style="left:333px;top:706px;width:140px;font-size:130px">の</span>

  <!-- left column -->
  <span class="glyph red" style="left:110px;top:135px;width:170px;font-size:162px">最</span>
  <span class="glyph red" style="left:110px;top:298px;width:170px;font-size:162px">強</span>
  <span class="glyph black" style="left:105px;top:474px;width:180px;font-size:176px">食</span>
  <span class="glyph black" style="left:105px;top:652px;width:180px;font-size:176px">品</span>

  <div class="author author-org">ルミナート口腔保健総合研究所</div>
  <div class="author author-role">歯科医師</div>
  <span class="author-name" style="left:34px;top:622px">杉</span>
  <span class="author-name" style="left:34px;top:670px">浦</span>
  <span class="author-name" style="left:34px;top:734px">航</span>
  <span class="author-name" style="left:34px;top:782px">平</span>

  <div class="band"></div>
  <div class="gift">読者プレゼント<small>つき</small></div>
  <div class="art" role="img" aria-label="チーズと歯のキャラクターが手をつなぐイラスト"></div>
  <div class="lead">歯科の専門家が伝えたい</div>
  <div class="catch catch-1">『チーズを食べれば</div>
  <div class="catch catch-2">歯は守れる!』</div>
</div>
</body>
</html>
```